A New and modern Business Card for Tarvish Commerce Partners Ltd

New and modern Logo and Business Card Attached is the current logo/business card designCurrently the business is called "Tarvish & Co." or TCP Ltd for short. This is subject to change.This business specialises in Telecoms and Energy. We work with the major networks (QX, Z7, etc) and also offer Energy Products saving clients money off their energy bills.These are business to business services.The current design incorporates a Pheonix, indicating rebirth, starting something new.We would like to maintain the Phoenix element but a newer modern style.We love colours in the logo 3 max.The aim of this is to be ultra slick and modern. I envisage Tarvish & Co. on one side of the card with long descriptions on the other side.Side 1:TCP Ltd/Logo?Side 2:TCP Ltd/Logo/Graphic?Brogan & Co.Name:Address:Phone:Email:The design is mostly flexible but must incorporate a Phoenix.For example "Tarvish & Co." with a block phoenix behind the text...up to you.

Industry/Entity Type

Telecommunications

Contact Information for Business Card

Tarvish & Co.
Address:
Name:
Phone:
Email:

Logo Text

Tarvish & Co.

Colors
33a6d7
0792cd
acd037
9bcb3c
f78f20
fece3e

Requirements
Must have
• Phoenix
• 3/4 colours max
• Blue representing Technology (wireless)
• Green for Eco Energy
• Orange for Phoenix
• White business card background
Should not have
• phoenix must not all be red/ orange fire, we are a technology service company and the phoenix colours must represent this. Fire is not representative of our company.

```html
<!DOCTYPE html>
<html lang="en">
<head>
<meta charset="UTF-8">
<title>Tarvish Commerce Partners Ltd – Business Card</title>
<link rel="stylesheet" href="https://fonts.googleapis.com/css2?family=Cinzel:wght@400;600&family=Open+Sans:wght@400;600&display=swap">
<style>
  :root {
    --stage: #ece9e4;
    --card-white: #ffffff;
    --tech-blue-light: #33a6d7;
    --tech-blue: #0792cd;
    --tech-blue-deep: #0578ab;
    --eco-green: #9bcb3c;
    --phoenix-orange: #f78f20;
    --rule: rgba(255, 255, 255, 0.6);
    --ink-light: #ffffff;
  }
  * { margin: 0; padding: 0; box-sizing: border-box; }
  html, body {
    width: 1200px;
    height: 900px;
    overflow: hidden;
    background: var(--stage);
  }
  .canvas {
    position: relative;
    width: 1200px;
    height: 900px;
  }
  .card {
    position: absolute;
    left: 330px;
    width: 557px;
    height: 343px;
    box-shadow: 3px 4px 8px rgba(0, 0, 0, 0.25);
  }
  .card--front {
    top: 90px;
    background: linear-gradient(180deg, var(--tech-blue-light) 0%, var(--tech-blue) 55%, var(--tech-blue-deep) 100%);
    color: var(--ink-light);
    text-align: center;
    font-family: "Open Sans", sans-serif;
  }
  .holder-name {
    position: absolute;
    top: 79px;
    left: 0;
    right: 0;
    font-family: "Cinzel", serif;
    font-size: 23px;
    font-weight: 400;
    letter-spacing: 0.5px;
    line-height: 28px;
  }
  .holder-role {
    position: absolute;
    top: 104px;
    left: 0;
    right: 0;
    font-size: 16px;
    line-height: 22px;
  }
  .divider {
    position: absolute;
    left: 180px;
    width: 196px;
    height: 1px;
    background: var(--rule);
  }
  .divider--upper { top: 136px; }
  .divider--lower { top: 204px; }
  .contact-lines {
    position: absolute;
    top: 148px;
    left: 0;
    right: 0;
    font-size: 16px;
    line-height: 21px;
    list-style: none;
  }
  .contact-lines strong { font-weight: 600; }
  .address {
    position: absolute;
    top: 220px;
    left: 0;
    right: 0;
    font-size: 16px;
    line-height: 21px;
    font-style: normal;
  }
  .card--back {
    top: 469px;
    background: var(--card-white);
    display: flex;
    flex-direction: column;
    align-items: center;
    justify-content: center;
    gap: 20px;
  }
  .brand-dot {
    width: 104px;
    height: 104px;
    border-radius: 50%;
    background: var(--phoenix-orange);
  }
  .brand-name {
    font-family: "Cinzel", serif;
    font-weight: 600;
    font-size: 24px;
    letter-spacing: 0.5px;
    color: var(--tech-blue);
    text-align: center;
    line-height: 30px;
  }
</style>
</head>
<body>
<main class="canvas">
  <section class="card card--front" aria-label="Card front: contact details">
    <h1 class="holder-name">MARCUS HALE</h1>
    <p class="holder-role">Managing Director</p>
    <div class="divider divider--upper"></div>
    <ul class="contact-lines">
      <li><strong>P:</strong> 044-987 654 321</li>
      <li><strong>E:</strong> hello@tarvishco.com</li>
    </ul>
    <div class="divider divider--lower"></div>
    <address class="address">12345, Address Goes Here<br>Country Name, 123456.</address>
  </section>

  <section class="card card--back" aria-label="Card back: brand">
    <div class="brand-dot" aria-hidden="true"></div>
    <p class="brand-name">TARVISH COMMERCE<br>PARTNERS LIMITED</p>
  </section>
</main>
</body>
</html>
```